Torvane Partners Brochure Design

Design a brochure for Torvane Partners, with a focus on the three key areas of the business:
- Business Advisory (consulting);
- Turnaround;
- Business Valuations.

Details in relation to the above available at www.torvanepartners-example.com

The aim of the document is to have something which works in a digital and physical form. The brochure should have each of the above areas on a separate A4 page so as to enable them to be presented digitally as stand alone brochures. Alternative designs which achieve the same will be accepted, I.e. Multiple brochures, one for whole of business and one for each business area.

Should also have a brief bio on Peter Lindgrove and Torvane Partners, also on a separate page or included in separate brochures if this approach is taken.

Industry/Entity Type

Digital

Requirements
Must have
• Please ensure that design flows from website.

```html
<!DOCTYPE html>
<html lang="en">
<head>
<meta charset="utf-8">
<title>Torvane Partners – Brochure Cover</title>
<link rel="stylesheet" href="https://fonts.googleapis.com/css2?family=Crimson+Text:wght@400&family=Questrial&display=swap">
<style>
  :root {
    --blue-light: #2277ab;
    --blue-dark: #173f86;
    --orange: #f39200;
    --orange-light: #fbb016;
    --navy-text: #1d3680;
    --white: #ffffff;
    --texture-tone: #e9ecef;
  }
  html, body {
    margin: 0;
    padding: 0;
    overflow: hidden;
    background: var(--white);
  }
  .cover {
    position: relative;
    width: 900px;
    height: 1200px;
    overflow: hidden;
    background: var(--white);
  }
  .cover__hero {
    position: absolute;
    left: 0; top: 0;
    width: 900px; height: 479px;
    background: linear-gradient(90deg, var(--blue-light) 0%, var(--blue-dark) 100%);
  }
  .cover__rule {
    position: absolute;
    left: 0; top: 479px;
    width: 900px; height: 7px;
    background: var(--orange);
  }
  .cover__texture {
    position: absolute;
    left: 0; top: 486px;
    width: 560px; height: 656px;
    background: radial-gradient(ellipse at 0% 10%, var(--texture-tone) 0%, rgba(255,255,255,0) 70%);
  }
  .services {
    position: absolute;
    right: 67px; top: 548px;
    margin: 0; padding: 0;
    list-style: none;
    text-align: right;
    font-family: "Crimson Text", Georgia, serif;
    font-size: 27px;
    color: var(--navy-text);
  }
  .services__item {
    line-height: 62.5px;
    letter-spacing: 0.3px;
  }
  .brand {
    position: absolute;
    right: 67px; top: 1010px;
    font-family: "Crimson Text", Georgia, serif;
    font-size: 44px;
    color: var(--navy-text);
    line-height: 1;
  }
  .brand-marker {
    position: absolute;
    left: 860px; top: 1033px;
    width: 40px; height: 24px;
  }
  .footer-band {
    position: absolute;
    left: 0; top: 1142px;
    width: 900px; height: 58px;
    background: linear-gradient(90deg, var(--orange) 0%, var(--orange-light) 100%);
  }
  .footer-band__url {
    position: absolute;
    right: 67px; top: 18px;
    font-family: "Questrial", Arial, sans-serif;
    font-size: 19px;
    letter-spacing: 2.2px;
    color: var(--white);
    text-transform: uppercase;
    line-height: 1;
  }
</style>
</head>
<body>
  <main class="cover">
    <div class="cover__hero"></div>
    <div class="cover__rule"></div>
    <div class="cover__texture" role="img" aria-label="Soft light grey halftone dot texture"></div>

    <ul class="services">
      <li class="services__item">Business Valuations</li>
      <li class="services__item">Business Turnaround</li>
      <li class="services__item">Due Diligence</li>
      <li class="services__item">Business Structuring</li>
    </ul>

    <div class="brand">Torvane Partners</div>
    <svg class="brand-marker" viewBox="0 0 40 24" aria-hidden="true">
      <line x1="12" y1="12" x2="40" y2="12" stroke="#1d3680" stroke-width="1.5"/>
      <circle cx="12" cy="12" r="10" fill="#1d4f8f"/>
    </svg>

    <footer class="footer-band">
      <span class="footer-band__url">www.torvanepartners-example.com</span>
    </footer>
  </main>
</body>
</html>
```